Retail Seafood business needs package/label design

In need of packaging/label design for multiple seafood products such as sword fish, halibut, cod fish, scallops, mahi, catfish, and lobster tails

```html
<!DOCTYPE html>
<html lang="en">
<head>
<meta charset="utf-8">
<title>Mackerel Package Label</title>
<link rel="stylesheet" href="https://fonts.googleapis.com/css2?family=Oswald:wght@500&family=Montserrat:wght@400;500;700&display=swap">
<style>
  :root {
    --paper: #ffffff;
    --cream: #f2dfc0;
    --berry: #b8324b;
    --ocean: #1d5b78;
    --ocean-soft: rgba(29, 91, 120, 0.22);
  }
  html, body {
    margin: 0;
    padding: 0;
    width: 1200px;
    height: 1199px;
    overflow: hidden;
    background: var(--paper);
  }
  .canvas {
    position: relative;
    width: 1200px;
    height: 1199px;
  }
  .label {
    position: absolute;
    left: 305px;
    top: 150px;
    width: 590px;
    height: 900px;
    background: var(--cream);
    box-shadow: 0 0 4px rgba(0, 0, 0, 0.14);
    overflow: hidden;
  }
  .brand-band {
    position: absolute;
    left: 417px;
    top: 0;
    width: 173px;
    height: 900px;
    background: var(--berry);
  }
  .brand-name {
    position: absolute;
    left: 448px;
    top: 74px;
    margin: 0;
    font-family: "Montserrat", sans-serif;
    font-weight: 500;
    font-size: 34px;
    line-height: 46px;
    color: var(--cream);
  }
  .headline {
    position: absolute;
    left: 40px;
    top: 52px;
    margin: 0;
    font-family: "Oswald", sans-serif;
    font-weight: 500;
    font-size: 72px;
    line-height: 70px;
    letter-spacing: -0.5px;
    color: var(--ocean);
    text-transform: uppercase;
    transform: scaleX(0.85);
    transform-origin: left top;
  }
  .variety {
    position: absolute;
    left: 275px;
    top: 64px;
    margin: 0;
    font-family: "Montserrat", sans-serif;
    font-weight: 700;
    font-size: 19px;
    letter-spacing: 2px;
    color: var(--berry);
  }
  .stamp {
    position: absolute;
    left: 181px;
    top: 167px;
    width: 116px;
    height: 116px;
  }
  .copy {
    position: absolute;
    left: 40px;
    margin: 0;
    font-family: "Montserrat", sans-serif;
    font-weight: 400;
    font-size: 12.6px;
    line-height: 16.4px;
    color: var(--ocean);
  }
  .copy-intro { top: 309px; width: 340px; }
  .copy-detail { top: 701px; width: 230px; }
  .illustration {
    position: absolute;
    left: 50px;
    top: 383px;
    width: 425px;
    height: 315px;
    border-radius: 40px;
    background: radial-gradient(ellipse at 55% 50%, var(--ocean-soft), rgba(29, 91, 120, 0.08));
  }
  .tagline {
    position: absolute;
    left: 40px;
    top: 813px;
    margin: 0;
    font-family: "Montserrat", sans-serif;
    font-weight: 700;
    font-size: 25px;
    letter-spacing: 3px;
    color: var(--berry);
  }
</style>
</head>
<body>
<main class="canvas">
  <section class="label">
    <div class="brand-band"></div>
    <p class="brand-name">Tide<br>Harbor</p>

    <h1 class="headline">Premium<br>Quality<br>Meat</h1>
    <p class="variety">MACKEREL</p>

    <svg class="stamp" viewBox="0 0 116 116" aria-label="Natural product stamp">
      <defs>
        <path id="stamp-ring" d="M38,92.64 A40,40 0 1,1 78,23.36 A40,40 0 1,1 38,92.64"/>
      </defs>
      <circle cx="58" cy="58" r="55" fill="#f2dfc0" stroke="var(--berry)" stroke-width="2.5"/>
      <circle cx="58" cy="58" r="21" fill="none" stroke="var(--berry)" stroke-width="2.5"/>
      <text font-family="Georgia, serif" font-size="17" fill="var(--berry)" letter-spacing="1.2">
        <textPath href="#stamp-ring" startOffset="1%">NATURAL PRODUCT</textPath>
      </text>
    </svg>

    <p class="copy copy-intro">Lorem ipsum dolor sit amet, consectetuer adipiscing elit. Cum sociis natoque penatibus et magnis dis parturient montes, nascetur ridiculus mus. Donec quam felis, ultricies nec, pellentesque eu, pretium quis, sem.</p>

    <div class="illustration" role="img" aria-label="Blue line illustration of a lobster seen from above, claws reaching into the red band"></div>

    <p class="copy copy-detail">Penatibus et magnis dis parturient montes, nascetur ridiculus mus. Donec quam felis, ultricies nec, pellentesque eu, pretium quis, sem.</p>

    <p class="tagline">PERFECT CHOICE</p>
  </section>
</main>
</body>
</html>
```